Shopping centre customer engagement software website

We need a multi page site with :

*What we do.
*How it works.
*Benefits
* Case study
* Testimonial
* Business login (we provide link to business portal)
* Consumer login (we provide link to consumer site)
* Book a demo
* Contact us

We want it to be clean and crisp and very self explanatory with little clutter. We are thinking white but are open to what ever looks the best.
Updates

Wordpress is preferred

Need extra days to review

Target Market(s)

Shopping centre managers and retail property companies

Coding

Coded - Design and coding required

Number of Pages Required

5+ page

Font styles to use
Sans Serif

Colors
ffffff

Requirements
Must have
• As listed above and must be responsive! Checkout our existing site for the text to be included (will be edited but it’ll give you an idea) www.vantrizo.com

```html
<!DOCTYPE html>
<html lang="en">
<head>
<meta charset="utf-8">
<title>Vantrizo – Shopping centre engagement</title>
<link href="https://fonts.googleapis.com/css2?family=Roboto:wght@300;400;500;700&display=swap" rel="stylesheet">
<style>
  :root{
    --white:#ffffff;
    --ink:#222427;
    --body:#3d4046;
    --muted:#7b7f86;
    --link:#6c7f93;
    --bar:#eeeff1;
    --rule:#d9dbde;
    --sky-top:#3a4756;
    --sky-mid:#6b7684;
    --city:#4a4a4c;
    --social:#8a93a0;
  }
  *{box-sizing:border-box;margin:0;padding:0}
  html,body{width:1200px;height:676px;overflow:hidden;background:var(--white)}
  body{font-family:"Roboto",Arial,sans-serif;color:var(--ink);position:relative}

  .hero{
    position:absolute;left:0;top:0;width:1200px;height:468px;
    background:linear-gradient(180deg,var(--sky-top) 0%,var(--sky-mid) 32%,#7c7f86 52%,#5b5854 72%,var(--city) 100%);
  }
  .hero-overlay{position:absolute;inset:0;background:linear-gradient(180deg,rgba(20,30,45,.55) 0%,rgba(20,30,45,.15) 30%,rgba(0,0,0,0) 60%)}

  .site-header{
    position:absolute;left:0;top:0;width:1200px;height:78px;
    display:flex;align-items:center;padding:0 46px;
    border-bottom:1px solid rgba(255,255,255,.35);
  }
  .brand{display:flex;align-items:center;gap:12px;color:var(--white);font-weight:300;font-size:30px;letter-spacing:2px}
  .brand-dot{width:40px;height:40px;border-radius:50%;background:var(--white);opacity:.85}
  .main-nav{display:flex;gap:34px;margin-left:140px}
  .main-nav a{color:var(--white);text-decoration:none;font-size:13.5px;font-weight:500;letter-spacing:-.2px}
  .logins{margin-left:auto;display:flex;gap:8px}
  .btn{font-size:13px;font-weight:500;border-radius:16px;padding:8px 22px;text-decoration:none}
  .btn-outline{color:var(--white);border:1.5px solid var(--white)}
  .btn-solid{color:var(--ink);background:var(--white);border:1.5px solid var(--white)}

  .hero-title{
    position:absolute;left:0;top:225px;width:1200px;text-align:center;
    color:var(--white);font-weight:300;font-size:23px;line-height:34px;
  }

  .sub-bar{
    position:absolute;left:0;top:468px;width:1200px;height:36px;background:var(--bar);
    border-bottom:1px solid var(--rule);display:flex;align-items:center;padding:0 46px;
    font-size:13px;
  }
  .sub-bar .label{color:var(--muted);margin-right:12px}
  .sub-bar a{color:var(--link);text-decoration:none;margin-right:22px}
  .sub-bar .tools{margin-left:auto;display:flex;gap:18px;align-items:center}
  .social{width:15px;height:15px;border-radius:3px;background:var(--social)}

  .what-we-do{position:absolute;left:46px;top:530px;width:560px}
  .what-we-do h1{font-size:32px;font-weight:500;margin-bottom:16px}
  .what-we-do p{font-size:13px;line-height:20px;color:var(--body);margin-bottom:16px}

  .app-preview{
    position:absolute;left:700px;top:540px;width:460px;height:136px;border-radius:8px 8px 0 0;
    background:linear-gradient(90deg,#e8eaed 0%,#f4f5f7 45%,#e9ebee 75%,#5b4a3c 100%);
  }
</style>
</head>
<body>
  <section class="hero">
    <div class="hero-overlay" role="img" aria-label="City skyline photograph with office towers under a cloudy sky"></div>

    <header class="site-header">
      <div class="brand"><span class="brand-dot"></span>VANTRIZO</div>
      <nav class="main-nav">
        <a href="#">HOW IT WORKS</a>
        <a href="#">BENEFITS</a>
        <a href="#">WHAT WE DO</a>
        <a href="#">CASE STUDY</a>
      </nav>
      <div class="logins">
        <a class="btn btn-outline" href="#">Consumer login</a>
        <a class="btn btn-solid" href="#">Business login</a>
      </div>
    </header>

    <h2 class="hero-title">Delight your shoppers, impress your tenants and<br>provide your landlords with accurate detailed<br>data in real time</h2>
  </section>

  <div class="sub-bar">
    <span class="label">Learn More:</span>
    <a href="#">Our Company</a>
    <a href="#">Testimonials</a>
    <a href="#">Careers</a>
    <a href="#">Help &amp; Contact</a>
    <div class="tools">
      <span class="social"></span>
      <span class="social"></span>
      <span class="social"></span>
      <svg width="14" height="14" viewBox="0 0 14 14" aria-label="Search"><circle cx="5.5" cy="5.5" r="4" fill="none" stroke="#8a93a0" stroke-width="1.8"/><line x1="8.5" y1="8.5" x2="13" y2="13" stroke="#8a93a0" stroke-width="2"/></svg>
    </div>
  </div>

  <section class="what-we-do">
    <h1>What we do</h1>
    <p>Vantrizo provides shopping centre managers with an easy to use platform which enables them to delight their shoppers, impress their tenants, provide detailed data to their landlords and all accessible to them at the click of button.</p>
    <p>Vantrizo gives shopping centres real time tracking through smart ID's of individual customer</p>
  </section>

  <div class="app-preview" role="img" aria-label="Row of app screens: mobile map view, shopping cart, checkout and a store collection page"></div>
</body>
</html>
```